E-Book-Cover für Ratgeber zum Thema Weisheit
Der Designer "pinselwerk" hat das Kunststück vollbracht, schon mit seinem ersten Entwurf genau ins Schwarze zu treffen, sodass nur noch Feinheiten abgestimmt werden mussten. Nach kleinen Wartezeiten ging er auf meine Wünsche ein und lieferte ein optimales Ergebnis ab, ohne dabei viele Worte zu verlieren. Er übermittelte mir eine farbige und eine schwarzweiße Variante des Designs in verschiedenen Dateiformaten. Ich kann diesen Designer nur empfehlen und würde wieder mit ihm arbeiten.
Zielgruppe
Ich bin ein experimenteller Schriftsteller, der ein E-Book über Lumora Self Press auf Varnello veröffentlichen möchte. Das Thema des Ratgebers ist Weisheit.
Weisheit gilt als ein eher antiquierter und abstrakter Begriff. Das ist ein Irrtum. Sie ist wichtiger als je zuvor und kann beschrieben werden. Weder ist sie gleichzusetzen mit Klugheit, noch mit spiritueller Erleuchtung. Sie beinhaltet bestimmte Eigenschaften wie Vernunft, Wissbegierde, Demut, Einfühlungsvermögen, Intuition, Auflehnung... Wobei rationales Denken das oberste Gebot ist. Es wird u.a. gezeigt, was Weisheit für das eigene Leben bringt und wie man sie anstreben kann.
Die Zielgruppe sind alle Menschen, die an Philosophie, Psychologie, Selbstoptimierung oder Religionen bzw. Atheismus interessiert sind. Menschen, die nach einer Erkenntnis oder 'Erleuchtung' suchen und etwas Besonderes in der Bücherflut entdecken möchten. Es ist weniger für Akademiker geschrieben; eher für die 'normale', durchschnittliche Bevölkerung und kann auch von bildungsferneren Schichten aller Altersgruppen verstanden werden.
Meine Vermutung ist, dass es bei offenen Personen mittleren Alters Anklang finden könnte.
Aufgabenstellung
Der Titel und der Untertitel des Buches müssen vorkommen (Titel: 'Das Stille Feuer'; Untertitel: 'Wie Sie durch einen kühnen Ansatz des klaren Handelns echte Stärke gewinnen'). Außerdem soll ein runder Button/Aufkleber/Sticker auf dem Cover kleben, welcher folgenden Text enthält: 'Mit Selbsttest! Wie weise bin ich?').
Natürlich soll der Name des Autors ebenfalls vorkommen: 'Till Brauner'
Das Cover soll sehr aus der Masse herausstechen, demnach ein echter Hingucker sein. Der potenzielle Kunde soll sofort neugierig sein! Es muss sowohl klein (als Thumbnail und am Smartphone), als auch groß gut aussehen und der Titel stets gut lesbar sein. Außerdem muss es schwarzweiß gut aussehen und erkennbar sein (für ebook-reader).
Varnello gibt folgende Werte für die Bilddatei vor: Die idealen Abmessungen für Coverdateien liegen bei 2 560 x 1 600 Pixeln. Mindestens 300 dpi. Die Größe der Bilddatei sollte 50MB nicht übersteigen. Farbprofil: RGB. DATEIFORMAT: JPG oder TIFF
Coverbilder mit weißem oder sehr hellem Hintergrund heben sich kaum vom Hintergrund ab. Fügen Sie einen dünnen Rahmen (3–4 Pixel) in Mittelgrau hinzu, um die Ränder des Coverbilds besser sichtbar zu machen.
Welches Cover gut zum Thema Weisheit passt, überlasse ich Ihrer Genialität. Ich dachte vielleicht an eine Art Blitz, Supernova, Erleuchtung, Explosion, geometrische Form o.ä. Aber Sie können sich etwas ganz eigenes ausdenken. Es sollte eher abstrakt sein. Außerdem muss es klar, edel und modern wirken, weniger comichaft oder verspielt/kitschig. Es darf etwas aggressiv bzw. 'revolutionär' wirken.

```html
<!DOCTYPE html>
<html lang="de">
<head>
<meta charset="utf-8">
<title>Das Stille Feuer – Till Brauner</title>
<link rel="stylesheet" href="https://fonts.googleapis.com/css2?family=Josefin+Sans:wght@300;400;600&display=swap">
<style>
  :root {
    --stage: #140811;
    --cover: #1e1d22;
    --cover-edge: #2a292f;
    --magenta: #d62ad6;
    --violet: #8a4cf0;
    --teal: #4fe3c4;
    --title: #f4f2f8;
  }
  * { margin: 0; padding: 0; box-sizing: border-box; }
  html, body {
    width: 1200px;
    height: 1055px;
    overflow: hidden;
    background: var(--stage);
    font-family: "Josefin Sans", sans-serif;
  }
  .cover {
    position: absolute;
    left: 293px;
    top: 77px;
    width: 613px;
    height: 900px;
    background: radial-gradient(ellipse at 50% 45%, #25232a 0%, var(--cover) 60%, #18171b 100%);
    border: 1px solid var(--cover-edge);
    overflow: hidden;
  }
  .subtitle {
    position: absolute;
    top: 52px;
    left: 0;
    width: 100%;
    text-align: center;
    color: var(--magenta);
    font-size: 13px;
    font-weight: 600;
    letter-spacing: 0.42em;
    padding-left: 0.42em;
    line-height: 24px;
    text-transform: uppercase;
  }
  .emblem {
    position: absolute;
    left: 0;
    top: 120px;
    width: 613px;
    height: 620px;
  }
  .title {
    position: absolute;
    top: 302px;
    left: 0;
    width: 100%;
    text-align: center;
    color: var(--title);
    font-weight: 400;
    text-transform: uppercase;
  }
  .title span {
    display: block;
    font-size: 26px;
    letter-spacing: 0.95em;
    line-height: 49px;
    padding-left: 0.95em;
  }
  .sticker-text {
    position: absolute;
    top: 468px;
    left: 0;
    width: 100%;
    text-align: center;
    font-size: 15px;
    font-weight: 300;
    letter-spacing: 0.35em;
    padding-left: 0.35em;
    line-height: 23px;
    color: var(--magenta);
    text-transform: uppercase;
  }
  .sticker-text span { display: block; }
  .sticker-text span:last-child { color: var(--violet); }
  .author {
    position: absolute;
    top: 804px;
    left: 0;
    width: 100%;
    text-align: center;
    font-size: 36px;
    font-weight: 300;
    letter-spacing: 0.38em;
    padding-left: 0.38em;
    text-transform: uppercase;
    background: linear-gradient(90deg, var(--magenta) 25%, var(--violet) 75%);
    -webkit-background-clip: text;
    background-clip: text;
    color: transparent;
  }
</style>
</head>
<body>
  <main class="cover">
    <p class="subtitle">Wie Sie durch einen kühnen<br>Ansatz des klaren Handelns<br>echte Stärke gewinnen</p>

    <svg class="emblem" viewBox="0 0 613 620">
      <defs>
        <linearGradient id="ring-stroke" x1="0" y1="0" x2="0" y2="1">
          <stop offset="0" stop-color="#2fb89a"/>
          <stop offset="0.55" stop-color="#4fe3c4"/>
          <stop offset="1" stop-color="#bff7ea"/>
        </linearGradient>
        <radialGradient id="light-glow" cx="0.5" cy="0.42" r="0.5">
          <stop offset="0.55" stop-color="#b9d2ff" stop-opacity="0.55"/>
          <stop offset="0.75" stop-color="#7a55d0" stop-opacity="0.35"/>
          <stop offset="1" stop-color="#4a1f6e" stop-opacity="0"/>
        </radialGradient>
        <filter id="soft" x="-20%" y="-20%" width="140%" height="140%">
          <feGaussianBlur stdDeviation="14"/>
        </filter>
        <filter id="glow" x="-20%" y="-20%" width="140%" height="140%">
          <feGaussianBlur stdDeviation="6"/>
        </filter>
      </defs>
      <ellipse class="light-trail" role="img"
               aria-label="Abstrakte Lichtstreifen, die vom leuchtenden Ring nach unten fließen"
               cx="306" cy="320" rx="265" ry="290"
               fill="url(#light-glow)" filter="url(#soft)"/>
      <circle cx="306" cy="270" r="214" fill="#141317"/>
      <circle cx="306" cy="270" r="214" fill="none" stroke="#4fe3c4" stroke-width="10" opacity="0.6" filter="url(#glow)"/>
      <circle cx="306" cy="270" r="214" fill="none" stroke="url(#ring-stroke)" stroke-width="4"/>
    </svg>

    <h1 class="title"><span>Das</span><span>Stille</span><span>Feuer</span></h1>

    <p class="sticker-text"><span>Mit Selbsttest!</span><span>Wie weise bin ich?</span></p>

    <p class="author">Till Brauner</p>
  </main>
</body>
</html>
```